Harbor Bundle Social Media Graphics

Focusing on the Evening Harbor Bundle product, create 6-7 individual social media graphics (square size). For the color scheme of the graphics, they should all be complementary with the Evening Harbor Bundle bottle colors.

Note: each graphic should have one of the pictures of the bottles (3 product bundle) on it and/or one of the images with a person on it (several pics attached)/only use stock photography that I provided.

Target Market(s)

women over 50 dealing with menopause

Industry/Entity Type

health and wellness

Requirements
Must have
• the pictures/images I provided

```html
<!DOCTYPE html>
<html lang="en">
<head>
<meta charset="utf-8">
<title>Harbor Bundle Social Media Graphics</title>
<link href="https://fonts.googleapis.com/css2?family=Poppins:wght@500;600;700;800&family=Montserrat:wght@600;700&display=swap" rel="stylesheet">
<style>
  :root{
    --stage:#8a8b8f;
    --paper-light:#f7f7f9;
    --paper-dark:#e4e4e8;
    --pink:#e8637a;
    --pink-soft:#f6c9d1;
    --mint:#93d5c0;
    --mint-soft:#d3eee5;
    --green:#3aa386;
    --ink:#1f1f22;
    --photo-warm:#b48a72;
    --photo-cool:#c9c6c4;
  }
  *{margin:0;padding:0;box-sizing:border-box}
  html,body{width:1200px;height:677px;overflow:hidden}
  body{background:var(--stage);position:relative;font-family:"Poppins",sans-serif;color:var(--ink)}

  .card{position:absolute;width:220px;height:220px;overflow:hidden;
    background:linear-gradient(135deg,var(--paper-light) 0%,#efeff2 55%,var(--paper-dark) 100%);
    box-shadow:0 2px 6px rgba(0,0,0,.22)}
  .card--hero{left:84px;top:216px;transform:scale(1.1);transform-origin:0 0}
  .card--weight{left:394px;top:95px}
  .card--symptoms{left:656px;top:95px}
  .card--relief{left:918px;top:95px}
  .card--solution{left:394px;top:356px}
  .card--flashes{left:656px;top:356px}
  .card--stop{left:918px;top:356px}

  .decor{position:absolute;inset:0;width:220px;height:220px}

  .brand{position:absolute;display:flex;align-items:center;gap:3px;
    font:600 6px/1 "Poppins",sans-serif;color:var(--green);white-space:nowrap}
  .brand::before{content:"";width:7px;height:7px;border-radius:50%;background:var(--mint)}

  .photo{position:absolute;border-radius:50%;border:5px solid var(--mint)}
  .photo--person{background:radial-gradient(circle at 50% 38%,var(--photo-warm) 0 22%,#7d7470 40%,var(--photo-cool) 75%)}
  .photo--product{background:radial-gradient(circle at 50% 55%,#ffffff 0 30%,#e9eeec 55%,#d6dbd9 100%)}
  .ring{position:absolute;border-radius:50%;border:2.5px solid transparent;
    border-left-color:var(--pink);border-top-color:var(--pink)}

  .txt{position:absolute;line-height:1;white-space:nowrap}
  .kicker{font:700 5.6px/1 "Montserrat",sans-serif;letter-spacing:1.8px}
  .h{font-weight:800;text-transform:uppercase}
  .pink{color:var(--pink)}
  .mint{color:var(--green)}
  .dark{color:var(--ink)}
  .right{text-align:right}
  .center{text-align:center}
  .small{font:500 5px/1.3 "Poppins",sans-serif}
  .rule{position:absolute;height:2px;border-radius:1px}
  .rule--pink{background:var(--pink)}
  .rule--mint{background:var(--mint)}
</style>
</head>
<body>

<!-- Hero post -->
<section class="card card--hero">
  <svg class="decor" viewBox="0 0 220 220" aria-hidden="true">
    <path d="M220 34 A46 46 0 0 0 220 126 Z" fill="#e8637a"/>
    <path d="M0 132 A40 40 0 0 1 0 212 Z" fill="#93d5c0"/>
    <polygon points="150,220 220,150 220,220" fill="#dcdce1" opacity=".6"/>
    <circle cx="176" cy="98" r="7" fill="#d3eee5"/>
    <circle cx="204" cy="206" r="5" fill="#e8637a"/>
  </svg>
  <span class="rule rule--pink" style="left:18px;top:20px;width:22px"></span>
  <span class="rule rule--mint" style="left:150px;top:54px;width:18px"></span>
  <div class="brand" style="right:10px;top:15px">Vital Bloom</div>
  <div class="ring" style="left:14px;top:24px;width:124px;height:124px;transform:rotate(-20deg)"></div>
  <div class="photo photo--person" style="left:20px;top:30px;width:114px;height:114px" role="img" aria-label="Portrait of a smiling woman with silver hair in a dark blazer"></div>
  <div class="txt kicker dark right" style="right:12px;top:143px">MENOPAUSAL OR</div>
  <div class="txt h mint right" style="right:11px;top:152px;font-size:14px">Post-Menopausal?</div>
  <div class="txt h dark right" style="right:11px;top:169px;font-size:13px">Get your <span class="pink">life back</span></div>
  <div class="txt small dark right" style="right:12px;top:185px">Menopause, Post-Menopause, or Hysterectomy<br>Symptoms? We’ve Got the Answer!</div>
</section>

<!-- Weight -->
<section class="card card--weight">
  <svg class="decor" viewBox="0 0 220 220" aria-hidden="true">
    <path d="M0 44 A30 30 0 0 1 0 104 Z" fill="#e8637a"/>
    <path d="M220 124 A36 36 0 0 0 220 196 Z" fill="#93d5c0"/>
    <circle cx="186" cy="112" r="6" fill="#f6c9d1"/>
    <circle cx="30" cy="208" r="6" fill="#e8637a"/>
  </svg>
  <span class="rule rule--pink" style="left:34px;top:47px;width:20px"></span>
  <span class="rule rule--mint" style="left:150px;top:192px;width:20px"></span>
  <div class="brand" style="left:16px;top:17px">Vital Bloom</div>
  <div class="txt kicker dark right" style="right:10px;top:20px">AN EASIER WAY TO</div>
  <div class="txt h pink right" style="right:10px;top:29px;font-size:14.5px">Lose weight</div>
  <div class="txt h mint right" style="right:10px;top:47px;font-size:14.5px">During</div>
  <div class="txt h dark right" style="right:10px;top:65px;font-size:14.5px">Menopause</div>
  <div class="ring" style="left:14px;top:82px;width:118px;height:118px;transform:rotate(-30deg)"></div>
  <div class="photo photo--person" style="left:20px;top:88px;width:106px;height:106px" role="img" aria-label="Smiling woman in a white top standing behind the three product bottles"></div>
</section>

<!-- Symptoms -->
<section class="card card--symptoms">
  <svg class="decor" viewBox="0 0 220 220" aria-hidden="true">
    <path d="M160 0 A40 40 0 0 0 220 40 L220 0 Z" fill="#e8637a"/>
    <path d="M0 98 A26 26 0 0 1 0 150 Z" fill="#93d5c0"/>
    <polygon points="190,60 220,30 220,220 150,220" fill="#dcdce1" opacity=".5"/>
    <circle cx="190" cy="62" r="6" fill="#d3eee5"/>
    <circle cx="28" cy="210" r="6" fill="#e8637a"/>
  </svg>
  <span class="rule rule--pink" style="left:30px;top:80px;width:14px"></span>
  <span class="rule rule--mint" style="left:170px;top:126px;width:18px"></span>
  <div class="brand" style="left:14px;top:16px">Vital Bloom</div>
  <div class="ring" style="left:60px;top:26px;width:100px;height:100px;transform:rotate(-60deg)"></div>
  <div class="photo photo--person" style="left:65px;top:31px;width:90px;height:90px" role="img" aria-label="Laughing woman with curly grey hair in a floral blouse"></div>
  <div class="txt kicker dark center" style="left:0;right:0;top:153px">STRUGGLING WITH</div>
  <div class="txt h mint center" style="left:0;right:0;top:162px;font-size:12.5px">Menopause symptoms?</div>
  <div class="txt h dark center" style="left:0;right:0;top:178px;font-size:7px;font-weight:700">The solution you’ve been</div>
  <div class="txt h pink center" style="left:0;right:0;top:187px;font-size:7px;font-weight:700">Waiting for!</div>
</section>

<!-- Relief -->
<section class="card card--relief">
  <svg class="decor" viewBox="0 0 220 220" aria-hidden="true">
    <path d="M220 52 A30 30 0 0 0 220 112 Z" fill="#e8637a"/>
    <polygon points="160,0 220,0 220,40" fill="#dcdce1" opacity=".6"/>
    <circle cx="164" cy="56" r="7" fill="#3aa386"/>
    <circle cx="30" cy="172" r="7" fill="#d3eee5"/>
  </svg>
  <span class="rule rule--mint" style="left:160px;top:94px;width:18px"></span>
  <span class="rule rule--pink" style="left:66px;top:184px;width:16px"></span>
  <div class="brand" style="right:10px;top:17px">Vital Bloom</div>
  <div class="ring" style="left:20px;top:20px;width:118px;height:118px;transform:rotate(200deg)"></div>
  <div class="photo photo--product" style="left:24px;top:24px;width:110px;height:110px" role="img" aria-label="The three-bottle Harbor Bundle: two pump bottles and a capsule jar"></div>
  <div class="txt h mint right" style="right:15px;top:134px;font-size:13px">Menopause</div>
  <div class="txt h dark right" style="right:15px;top:150px;font-size:15px">Relief is here</div>
  <div class="txt h pink right" style="right:15px;top:168px;font-size:8.5px;font-weight:600">Get your life</div>
  <div class="txt h dark right" style="right:15px;top:180px;font-size:12.5px">Back today!</div>
</section>

<!-- Solution -->
<section class="card card--solution">
  <svg class="decor" viewBox="0 0 220 220" aria-hidden="true">
    <path d="M0 32 A28 28 0 0 1 0 88 Z" fill="#93d5c0"/>
    <path d="M220 132 A30 30 0 0 0 220 192 Z" fill="#e8637a"/>
    <polygon points="170,0 220,0 220,60" fill="#dcdce1" opacity=".6"/>
    <circle cx="52" cy="28" r="6" fill="#f6c9d1"/>
  </svg>
  <span class="rule rule--pink" style="left:44px;top:66px;width:20px"></span>
  <span class="rule rule--mint" style="left:160px;top:180px;width:20px"></span>
  <div class="ring" style="left:78px;top:24px;width:124px;height:124px;transform:rotate(30deg)"></div>
  <div class="photo photo--person" style="left:82px;top:28px;width:116px;height:116px" role="img" aria-label="Smiling older woman with short grey hair in a pink jacket"></div>
  <div class="brand" style="left:26px;top:114px">Vital Bloom</div>
  <div class="txt h dark" style="left:24px;top:138px;font-size:15px">The</div>
  <div class="txt h mint" style="left:24px;top:156px;font-size:16px">Menopause</div>
  <div class="txt h dark" style="left:24px;top:176px;font-size:8px;font-weight:600;line-height:1.25">Solution you’ve<br>been <span class="pink">waiting</span> for is here!</div>
</section>

<!-- Flashes -->
<section class="card card--flashes">
  <svg class="decor" viewBox="0 0 220 220" aria-hidden="true">
    <path d="M220 18 A30 30 0 0 0 220 78 Z" fill="#93d5c0"/>
    <path d="M0 164 A56 56 0 0 1 56 220 L0 220 Z" fill="#e8637a"/>
    <circle cx="28" cy="24" r="7" fill="#e8637a"/>
    <circle cx="194" cy="196" r="6" fill="#d3eee5"/>
  </svg>
  <span class="rule rule--mint" style="left:16px;top:110px;width:14px"></span>
  <span class="rule rule--pink" style="left:178px;top:100px;width:18px"></span>
  <div class="brand" style="left:88px;top:12px">Vital Bloom</div>
  <div class="txt kicker dark center" style="left:0;right:0;top:32px">SAY GOODBYE</div>
  <div class="txt h mint center" style="left:0;right:0;top:40px;font-size:13.5px">To hot flashes and</div>
  <div class="txt h dark center" style="left:0;right:0;top:57px;font-size:7.5px;font-weight:700">Night sweats for good!</div>
  <div class="ring" style="left:42px;top:76px;width:136px;height:136px;transform:rotate(40deg)"></div>
  <div class="photo photo--product" style="left:48px;top:82px;width:124px;height:124px" role="img" aria-label="The three Harbor Bundle bottles standing side by side"></div>
</section>

<!-- Stop -->
<section class="card card--stop">
  <svg class="decor" viewBox="0 0 220 220" aria-hidden="true">
    <path d="M220 40 A30 30 0 0 0 220 100 Z" fill="#93d5c0"/>
    <path d="M20 220 A36 36 0 0 1 92 220 Z" fill="#e8637a"/>
    <circle cx="30" cy="144" r="6" fill="#d3eee5"/>
    <circle cx="186" cy="210" r="6" fill="#e8637a"/>
  </svg>
  <span class="rule rule--pink" style="left:176px;top:50px;width:18px"></span>
  <span class="rule rule--mint" style="left:46px;top:172px;width:18px"></span>
  <div class="brand" style="right:10px;top:16px">Vital Bloom</div>
  <div class="txt dark" style="left:13px;top:22px;font:600 11px/1 'Montserrat',sans-serif;letter-spacing:3px">STOP</div>
  <div class="txt h mint" style="left:13px;top:37px;font-size:14px">Menopause</div>
  <div class="txt h pink" style="left:13px;top:53px;font-size:15.5px">Weight gain</div>
  <div class="txt h dark" style="left:13px;top:72px;font-size:8.5px;font-weight:700">In its tracks!</div>
  <div class="ring" style="left:88px;top:86px;width:126px;height:126px;transform:rotate(220deg)"></div>
  <div class="photo photo--person" style="left:93px;top:91px;width:116px;height:116px" role="img" aria-label="Smiling woman in a brown top holding two of the product bottles"></div>
</section>

</body>
</html>
```